Social Media Application Design - Android and IOS

I am ready to go live with new social media app however I am not comfortable with the current design. It is a not interactive or attractive enough. Please note the splash screen is a green, so preference would be to keep a green theme although I am more than happy to consider other colours that would improve the design.
The attachment has the app screens that need to be redesigned. They may not need massive changes , however keen to go live so looking for inspired designers to support with this project and many others that I have, including ongoing work on this app.
Target Market(s)
Millenials
Industry/Entity Type
Social
Colors
Designer to choose colors to be used in the design.
Requirements
Must have
- Please see attached document for screens that I would like redesigned. It needs to work with Android and IOS. I am looking for the design and not the functionality.
Nice to have
- Highly interactive design. Please see polling functionality of Pictavo.
Should not have
- should not be complicated - simplicity is the key

```html
<!DOCTYPE html>
<html lang="en">
<head>
<meta charset="utf-8">
<title>Post a Question – App Screens</title>
<link href="https://fonts.googleapis.com/css2?family=Roboto:wght@400;500;700&display=swap" rel="stylesheet">
<style>
  :root {
    --indigo: #2e3192;
    --indigo-light: #4549a3;
    --screen-bg: #efeff6;
    --canvas-bg: #f6f6f8;
    --ink: #2b2b33;
    --muted: #9a9aa8;
    --line: #c9c9d6;
    --tile: #c8c9e6;
    --badge: #e02424;
  }
  * { box-sizing: border-box; margin: 0; padding: 0; }
  html, body { width: 1200px; height: 1200px; overflow: hidden; }
  body {
    background: var(--canvas-bg);
    font-family: "Roboto", Arial, sans-serif;
    color: var(--ink);
    position: relative;
  }
  .screen {
    position: absolute;
    width: 330px; height: 560px;
    background: var(--screen-bg);
    border-radius: 6px;
    overflow: hidden;
    box-shadow: 0 12px 30px rgba(40, 40, 80, .18);
  }
  .app-bar {
    position: absolute; left: 0; top: 0; width: 100%; height: 78px;
    background: linear-gradient(100deg, var(--indigo) 0 55%, var(--indigo-light) 55% 100%);
    color: #fff;
  }
  .status-bar {
    position: absolute; left: 0; top: 0; width: 100%; height: 20px;
    display: flex; align-items: center; justify-content: space-between;
    padding: 0 10px; font-size: 9px; color: rgba(255,255,255,.8);
  }
  .app-bar .back { position: absolute; left: 14px; top: 34px; }
  .app-bar .title { position: absolute; left: 0; right: 0; top: 44px; text-align: center; font-size: 13px; font-weight: 500; }
  .app-bar .search { position: absolute; right: 14px; top: 42px; }
  .heading { position: absolute; left: 20px; font-size: 17px; font-weight: 700; letter-spacing: .3px; }
  .chips { position: absolute; left: 20px; right: 20px; display: flex; flex-wrap: wrap; gap: 10px; }
  .chip {
    border: 1.5px solid var(--indigo); color: var(--indigo);
    font-size: 11.5px; font-weight: 500; padding: 6px 14px; border-radius: 2px; background: transparent;
  }
  .chip.is-active { background: var(--indigo); color: #fff; }
  .field {
    position: absolute; left: 20px; right: 20px;
    border: 1px solid var(--line); background: #f5f5fa; border-radius: 2px;
    font-size: 10px; color: var(--muted); padding: 8px 10px;
  }
  .field .chev { position: absolute; right: 10px; top: 50%; transform: translateY(-50%); }
  .btn-post, .btn-next {
    position: absolute; right: 20px; bottom: 22px;
    background: var(--indigo); color: #fff; font-size: 13px; font-weight: 500;
    padding: 10px 16px; width: 104px; display: flex; justify-content: space-between; align-items: center; border-radius: 2px;
  }
  .tile {
    position: absolute; width: 130px; height: 70px; border-radius: 2px;
    display: flex; align-items: center; justify-content: center;
  }
  .tile.is-filled { background: var(--tile); }
  .tile.is-empty { border: 1px solid var(--line); background: #f5f5fa; }
  .tile-label { position: absolute; font-size: 9px; font-weight: 700; color: var(--indigo); }
  .link { position: absolute; left: 20px; font-size: 11px; color: var(--indigo); text-decoration: underline; }

  /* drawer */
  .profile-photo {
    position: absolute; left: 0; top: 0; width: 100%; height: 210px;
    background: linear-gradient(160deg, #3a3d44 0%, #5a5f6e 45%, #b99a38 75%, #2f3037 100%);
  }
  .profile-name { position: absolute; left: 22px; top: 226px; font-size: 18px; }
  .profile-mail { position: absolute; left: 22px; top: 250px; font-size: 10px; color: var(--muted); }
  .menu { position: absolute; left: 22px; right: 22px; top: 284px; list-style: none; }
  .menu li {
    display: flex; align-items: center; gap: 14px; height: 34px; font-size: 13px;
    border-bottom: 1px solid #e1e1ea;
  }
  .menu .icon { width: 14px; height: 14px; position: relative; }
  .badge {
    position: absolute; left: -4px; top: -6px; width: 11px; height: 11px; border-radius: 50%;
    background: var(--badge); color: #fff; font-size: 7px; text-align: center; line-height: 11px;
  }
  .toggle { position: absolute; right: 26px; bottom: 26px; width: 34px; height: 16px; border-radius: 8px; background: #b9bbe0; }
  .toggle::after { content: ""; position: absolute; right: 0; top: -2px; width: 20px; height: 20px; border-radius: 50%; background: var(--indigo); }
</style>
</head>
<body>

<!-- Screen: navigation drawer -->
<section class="screen" style="left:45px; top:30px;">
  <div class="profile-photo" role="img" aria-label="Profile photo of the user sitting on a yellow sofa"></div>
  <div class="status-bar"><span>●●●●○ FFF</span><span>100% ▭</span></div>
  <svg class="back" style="position:absolute;left:14px;top:30px" width="18" height="14" viewBox="0 0 18 14"><path d="M17 7H2M7 1 1 7l6 6" stroke="#fff" stroke-width="2" fill="none"/></svg>
  <div class="profile-name">Daniel Moore</div>
  <div class="profile-mail">daniel.moore@mailbox.com</div>
  <ul class="menu">
    <li><svg class="icon" viewBox="0 0 14 14"><circle cx="7" cy="7" r="5" stroke="#999" fill="none" stroke-width="1.4"/></svg>Home</li>
    <li><svg class="icon" viewBox="0 0 14 14"><circle cx="7" cy="4.5" r="2.8" fill="#999"/><path d="M2 13a5 5 0 0 1 10 0z" fill="#999"/></svg>My Profile</li>
    <li><svg class="icon" viewBox="0 0 14 14"><path d="M1 12h12M2 10l3-4 3 2 4-5" stroke="#999" fill="none" stroke-width="1.4"/></svg>My Activities</li>
    <li><span class="icon"><svg viewBox="0 0 14 14" width="14" height="14"><path d="M3 10V6a4 4 0 0 1 8 0v4l1 1H2z" fill="#999"/></svg><span class="badge">2</span></span>Notifications</li>
    <li><svg class="icon" viewBox="0 0 14 14"><path d="M3 1l3 3-2 2a8 8 0 0 0 4 4l2-2 3 3-2 2C6 13 1 8 1 3z" fill="#999"/></svg>Contact Us</li>
    <li><svg class="icon" viewBox="0 0 14 14"><path d="M8 2H2v10h6M6 7h7M10 4l3 3-3 3" stroke="#999" fill="none" stroke-width="1.4"/></svg>Log Out</li>
  </ul>
  <div class="toggle"></div>
</section>

<!-- Screen: choose topics -->
<section class="screen" style="left:435px; top:30px;">
  <header class="app-bar">
    <div class="status-bar"><span>●●●●○ FFF</span><span>100% ▭</span></div>
    <svg class="back" width="18" height="14" viewBox="0 0 18 14"><path d="M17 7H2M7 1 1 7l6 6" stroke="#fff" stroke-width="2" fill="none"/></svg>
    <div class="title">Post a Question</div>
    <svg class="search" width="16" height="16" viewBox="0 0 16 16"><circle cx="7" cy="7" r="5" stroke="#fff" stroke-width="2" fill="none"/><path d="M11 11l4 4" stroke="#fff" stroke-width="2"/></svg>
  </header>
  <h2 class="heading" style="top:98px;">What is your question about?</h2>
  <div class="chips" style="top:140px;">
    <span class="chip">Science</span><span class="chip">Health</span><span class="chip is-active">Technology</span>
    <span class="chip is-active">Travel</span><span class="chip">Fashion</span><span class="chip">Gedgets</span>
    <span class="chip">Language</span><span class="chip">Religion</span><span class="chip">Beauty</span>
    <span class="chip is-active">Finance</span><span class="chip">Education</span><span class="chip">History</span>
    <span class="chip">My Country</span><span class="chip">Business</span><span class="chip">My Cities</span>
  </div>
  <div class="btn-next">Next <svg width="14" height="12" viewBox="0 0 14 12"><path d="M1 6h11M8 2l4 4-4 4" stroke="#fff" stroke-width="1.8" fill="none"/></svg></div>
</section>

<!-- Screen: image options -->
<section class="screen" style="left:825px; top:30px;">
  <header class="app-bar">
    <div class="status-bar"><span>●●●●○ FFF</span><span>100% ▭</span></div>
    <svg class="back" width="18" height="14" viewBox="0 0 18 14"><path d="M17 7H2M7 1 1 7l6 6" stroke="#fff" stroke-width="2" fill="none"/></svg>
    <div class="title">Post a Question</div>
    <svg class="search" width="16" height="16" viewBox="0 0 16 16"><circle cx="7" cy="7" r="5" stroke="#fff" stroke-width="2" fill="none"/><path d="M11 11l4 4" stroke="#fff" stroke-width="2"/></svg>
  </header>
  <h2 class="heading" style="top:94px;">Your question is about</h2>
  <div class="chips" style="top:124px;"><span class="chip is-active">Technology</span><span class="chip is-active">Travel</span><span class="chip is-active">Finance</span></div>
  <h2 class="heading" style="top:168px;">What is your question?</h2>
  <div class="field" style="top:198px; height:90px;">Type question ...</div>
  <h2 class="heading" style="top:304px;">What are the options?</h2>
  <div class="field" style="top:336px; height:32px;">Images<svg class="chev" width="10" height="6" viewBox="0 0 10 6"><path d="M1 1l4 4 4-4" stroke="#2e3192" stroke-width="1.5" fill="none"/></svg></div>
  <div class="tile is-filled" style="left:20px; top:384px;"><svg width="26" height="20" viewBox="0 0 26 20"><rect width="26" height="20" rx="2" fill="#2e3192" opacity=".55"/><path d="M3 17l7-8 5 5 3-3 5 6z" fill="#fff"/></svg></div>
  <div class="tile-label" style="left:20px; top:460px;">Upload Image</div>
  <div class="tile is-empty" style="left:180px; top:384px;"><svg width="20" height="20" viewBox="0 0 20 20"><path d="M10 2v16M2 10h16" stroke="#2e3192" stroke-width="2"/></svg></div>
  <div class="btn-post">Post <svg width="14" height="12" viewBox="0 0 14 12"><path d="M1 1l12 5-12 5 3-5z" fill="#fff"/></svg></div>
</section>

<!-- Screen: text options -->
<section class="screen" style="left:240px; top:620px;">
  <header class="app-bar">
    <div class="status-bar"><span>●●●●○ FFF</span><span>100% ▭</span></div>
    <svg class="back" width="18" height="14" viewBox="0 0 18 14"><path d="M17 7H2M7 1 1 7l6 6" stroke="#fff" stroke-width="2" fill="none"/></svg>
    <div class="title">Post a Question</div>
    <svg class="search" width="16" height="16" viewBox="0 0 16 16"><circle cx="7" cy="7" r="5" stroke="#fff" stroke-width="2" fill="none"/><path d="M11 11l4 4" stroke="#fff" stroke-width="2"/></svg>
  </header>
  <h2 class="heading" style="top:94px;">Your question is about</h2>
  <div class="chips" style="top:124px;"><span class="chip is-active">Technology</span><span class="chip is-active">Travel</span><span class="chip is-active">Finance</span></div>
  <h2 class="heading" style="top:168px;">What is your question?</h2>
  <div class="field" style="top:198px; height:90px;">Type question ...</div>
  <h2 class="heading" style="top:304px;">What are the options?</h2>
  <div class="field" style="top:336px; height:32px;">Text<svg class="chev" width="10" height="6" viewBox="0 0 10 6"><path d="M1 1l4 4 4-4" stroke="#2e3192" stroke-width="1.5" fill="none"/></svg></div>
  <div class="field" style="top:382px; height:80px;">Type option ...</div>
  <div class="link" style="top:474px;">Add Text line</div>
  <div class="btn-post">Post <svg width="14" height="12" viewBox="0 0 14 12"><path d="M1 1l12 5-12 5 3-5z" fill="#fff"/></svg></div>
</section>

<!-- Screen: audio options -->
<section class="screen" style="left:630px; top:620px;">
  <header class="app-bar">
    <div class="status-bar"><span>●●●●○ FFF</span><span>100% ▭</span></div>
    <svg class="back" width="18" height="14" viewBox="0 0 18 14"><path d="M17 7H2M7 1 1 7l6 6" stroke="#fff" stroke-width="2" fill="none"/></svg>
    <div class="title">Post a Question</div>
    <svg class="search" width="16" height="16" viewBox="0 0 16 16"><circle cx="7" cy="7" r="5" stroke="#fff" stroke-width="2" fill="none"/><path d="M11 11l4 4" stroke="#fff" stroke-width="2"/></svg>
  </header>
  <h2 class="heading" style="top:94px;">Your question is about</h2>
  <div class="chips" style="top:124px;"><span class="chip is-active">Technology</span><span class="chip is-active">Travel</span><span class="chip is-active">Finance</span></div>
  <h2 class="heading" style="top:168px;">What is your question?</h2>
  <div class="field" style="top:198px; height:90px;">Type question ...</div>
  <h2 class="heading" style="top:304px;">What are the options?</h2>
  <div class="field" style="top:336px; height:32px;">Images<svg class="chev" width="10" height="6" viewBox="0 0 10 6"><path d="M1 1l4 4 4-4" stroke="#2e3192" stroke-width="1.5" fill="none"/></svg></div>
  <div class="tile is-filled" style="left:20px; top:384px; justify-content:space-between; padding:0 14px; font-size:11px;"><span>0:30</span><svg width="14" height="20" viewBox="0 0 14 20"><rect x="3" y="0" width="8" height="13" rx="4" fill="#2e3192"/><path d="M1 9a6 6 0 0 0 12 0M7 15v4" stroke="#2e3192" stroke-width="1.6" fill="none"/></svg></div>
  <div class="tile-label" style="left:20px; top:460px;">Record Option 1</div>
  <div class="tile is-empty" style="left:180px; top:384px; justify-content:space-between; padding:0 12px; font-size:9px; color:#2b2b33;"><span>Hold to Record</span><svg width="18" height="18" viewBox="0 0 20 20"><path d="M10 2v16M2 10h16" stroke="#2e3192" stroke-width="2"/></svg></div>
  <div class="tile-label" style="left:180px; top:460px;">Record Option 2</div>
  <div class="btn-post">Post <svg width="14" height="12" viewBox="0 0 14 12"><path d="M1 1l12 5-12 5 3-5z" fill="#fff"/></svg></div>
</section>

</body>
</html>
```